Delia Morvan
exclusive handcrafted jewelry
Simple
delmorvan@quillbox.net
deliamorvandesign.net
business card should be shaded black like uploaded logo.
I also like the royal blue option !
I have no idea what is on that file since I can not open it . I hope it is my logo in blue or shaded black.

```html
<!DOCTYPE html>
<html lang="en">
<head>
<meta charset="utf-8">
<title>Delia Morvan — Stationery Set</title>
<link href="https://fonts.googleapis.com/css2?family=Montserrat:wght@400;500;600&display=swap" rel="stylesheet">
<style>
  :root {
    --backdrop: #e8e3db;
    --paper: #ffffff;
    --navy-deep: #0b0b2c;
    --navy: #1b1b55;
    --navy-glow: #3b3b8e;
    --ink: #2a2a2a;
    --ink-soft: #8a8a8a;
    --on-navy: #ffffff;
    --shadow: rgba(40, 30, 20, 0.22);
  }
  * { box-sizing: border-box; margin: 0; padding: 0; }
  html, body { width: 1200px; height: 906px; overflow: hidden; }
  body {
    background: var(--backdrop);
    font-family: "Montserrat", Arial, sans-serif;
    color: var(--ink);
    position: relative;
  }
  .sheet {
    position: absolute;
    background: var(--paper);
    box-shadow: 0 4px 14px var(--shadow);
    overflow: hidden;
  }
  .navy-band {
    position: absolute;
    left: 0; right: 0;
    background: radial-gradient(ellipse at 50% 50%, var(--navy-glow) 0%, var(--navy) 45%, var(--navy-deep) 100%);
  }
  .wordmark {
    position: absolute;
    text-align: center;
    font-weight: 500;
    letter-spacing: 0.04em;
  }
  .wordmark .name { display: block; }
  .wordmark .tagline {
    display: block;
    font-size: 0.32em;
    letter-spacing: 0.18em;
    text-transform: uppercase;
    margin-top: 0.35em;
    color: var(--ink-soft);
  }
  .contact {
    position: absolute;
    color: var(--on-navy);
    font-size: 8px;
    white-space: nowrap;
  }
  .contact b { font-weight: 600; }
  .curve { position: absolute; left: 0; width: 100%; display: block; }

  /* Letterhead */
  .letterhead { left: 34px; top: 34px; width: 580px; height: 830px; }
  .letterhead .wordmark { left: 0; right: 0; top: 70px; font-size: 30px; }
  .letterhead .curve { bottom: 0; height: 70px; }
  .letterhead .contact { left: 22px; bottom: 16px; }

  /* Envelope back */
  .envelope-back { left: 562px; top: 138px; width: 606px; height: 390px; }
  .envelope-back .flap { top: 0; height: 100px; }
  .envelope-back .flap-name {
    position: absolute; left: 0; right: 0; top: 38px;
    text-align: center; color: var(--on-navy); font-size: 16px; font-weight: 500; letter-spacing: 0.06em;
  }
  .envelope-back .wordmark { left: 24px; top: 135px; font-size: 28px; text-align: left; }
  .envelope-back .curve { bottom: 0; height: 90px; }
  .envelope-back .contact { left: 24px; bottom: 48px; }

  /* Envelope front */
  .envelope-front { left: 566px; top: 522px; width: 602px; height: 276px; }
  .envelope-front .flap { top: 0; height: 100px; }
  .envelope-front .flap-name {
    position: absolute; left: 0; right: 0; top: 40px;
    text-align: center; color: var(--on-navy); font-size: 16px; font-weight: 500; letter-spacing: 0.06em;
  }

  /* Business card */
  .business-card {
    left: 722px; top: 704px; width: 286px; height: 150px;
    border-radius: 6px;
    background: radial-gradient(ellipse at 50% 40%, var(--navy-glow) 0%, var(--navy) 40%, var(--navy-deep) 100%);
  }
  .business-card .wordmark { left: 0; right: 0; top: 44px; font-size: 18px; color: var(--on-navy); }
  .business-card .wordmark .tagline { color: #c9c9e0; }
  .business-card .contact { left: 0; right: 0; text-align: center; top: 112px; font-size: 7px; line-height: 1.5; }
</style>
</head>
<body>

  <section class="sheet letterhead" aria-label="Letterhead">
    <div class="wordmark">
      <span class="name">Delia Morvan</span>
      <span class="tagline">Exclusive handcrafted jewelry</span>
    </div>
    <svg class="curve" viewBox="0 0 580 70" preserveAspectRatio="none" aria-hidden="true">
      <defs>
        <linearGradient id="lhBand" x1="0" y1="0" x2="1" y2="0">
          <stop offset="0" stop-color="#0b0b2c"/><stop offset="0.5" stop-color="#2a2a78"/><stop offset="1" stop-color="#0b0b2c"/>
        </linearGradient>
      </defs>
      <path d="M0 40 Q290 -10 580 30 L580 70 L0 70 Z" fill="url(#lhBand)"/>
    </svg>
    <p class="contact"><b>Phone:</b> 555-014-2297 | <b>Email:</b> delmorvan@quillbox.net | www.deliamorvandesign.net</p>
  </section>

  <section class="sheet envelope-back" aria-label="Envelope with flap">
    <div class="navy-band flap"><span class="flap-name">Delia Morvan</span></div>
    <div class="wordmark">
      <span class="name">Delia Morvan</span>
      <span class="tagline">Exclusive handcrafted jewelry</span>
    </div>
    <svg class="curve" viewBox="0 0 606 90" preserveAspectRatio="none" aria-hidden="true">
      <defs>
        <linearGradient id="envBand" x1="0" y1="0" x2="1" y2="0">
          <stop offset="0" stop-color="#0b0b2c"/><stop offset="0.5" stop-color="#2a2a78"/><stop offset="1" stop-color="#0b0b2c"/>
        </linearGradient>
      </defs>
      <path d="M0 26 Q303 4 606 30 L606 90 L0 90 Z" fill="url(#envBand)"/>
    </svg>
    <p class="contact"><b>Phone:</b> 555-014-2297 | <b>Email:</b> delmorvan@quillbox.net | www.deliamorvandesign.net</p>
  </section>

  <section class="sheet envelope-front" aria-label="Envelope back">
    <div class="navy-band flap"><span class="flap-name">Delia Morvan</span></div>
  </section>

  <section class="sheet business-card" aria-label="Business card">
    <div class="wordmark">
      <span class="name">Delia Morvan</span>
      <span class="tagline">Exclusive handcrafted jewelry</span>
    </div>
    <p class="contact"><b>Phone:</b> 555-014-2297 | <b>Email:</b> delmorvan@quillbox.net<br>www.deliamorvandesign.net</p>
  </section>

</body>
</html>
```